Reef Glow

sunglasses, sihoullette of body, maybe wearing a bikini or sunglasses. I am offering spray tanning, body wraps, tanning beds, stand up, body art, airbrush makeup.

Target Market(s)

I would say my target is all ages, But tanning is a seasonal business and more beauty and aging concept. and around prom time I get my most profitable business. so 18 to 21 through march and april. then 25 to 55 through april to june.

Industry/Entity Type

Makeup

Contact Information for Business Card

Phone number: 701-555-0147 Owner: Jan Mortby (Lisowski)

Colors

Designer to choose colors to be used in the design.

Requirements
Nice to have
• Sunglasses, silouttes of body wearing sunglasses or bikini, or picture of spray gun.

```html
<!DOCTYPE html>
<html lang="en">
<head>
<meta charset="utf-8">
<title>Reef Glow – Business Card</title>
<link rel="stylesheet" href="https://fonts.googleapis.com/css2?family=Open+Sans:wdth,wght@75..100,600;75..100,700&display=swap">
<style>
  :root {
    --page-bg: #dcdcdc;
    --card-teal: #7fbdc5;
    --brand-tint: #a9d3d0;
    --text-cream: #fdf8ea;
    --bloom-light: #f6ecb4;
    --bloom-gold: #e9bd3e;
    --bloom-orange: #d9772f;
  }
  html, body {
    margin: 0;
    width: 900px;
    height: 1200px;
    overflow: hidden;
    background: var(--page-bg);
  }
  .card {
    position: absolute;
    left: 45px;
    top: 340px;
    width: 810px;
    height: 520px;
    background: var(--card-teal);
    overflow: hidden;
    font-family: "Open Sans", Arial, sans-serif;
  }
  .bloom-area {
    position: absolute;
    left: -234px;
    top: -36px;
    width: 600px;
    height: 600px;
    border-radius: 50%;
    background: radial-gradient(circle at center,
      var(--bloom-light) 0%,
      var(--bloom-light) 40%,
      var(--bloom-gold) 62%,
      var(--bloom-gold) 86%,
      var(--bloom-orange) 100%);
  }
  .brand-name {
    position: absolute;
    right: 40px;
    top: 18px;
    margin: 0;
    font-size: 96px;
    font-weight: 700;
    font-stretch: 75%;
    letter-spacing: -1px;
    line-height: 1;
    text-transform: uppercase;
    color: var(--brand-tint);
  }
  .contact {
    position: absolute;
    left: 430px;
    top: 210px;
    color: var(--text-cream);
    font-weight: 700;
  }
  .contact-name {
    margin: 0 0 8px;
    font-size: 31px;
    line-height: 1.2;
  }
  .contact-phone {
    margin: 0;
    font-size: 26px;
    line-height: 1.2;
  }
</style>
</head>
<body>
  <div class="card">
    <div class="bloom-area" role="img" aria-label="Geometric sun flower with cream, gold and orange petals"></div>
    <p class="brand-name">Reef Glow</p>
    <div class="contact">
      <p class="contact-name">Jan Mortby (Lisowski)</p>
      <p class="contact-phone">Phone: 701-555-0147</p>
    </div>
  </div>
</body>
</html>
```